Velmora Farm's Tidewell Organic Fertilizer Label Design

This product is an organic fertilizer derived from a vermiculture process. This product is an alternative to oil based fertilizers and is safe for Gardens, Lawns and for the ag industry. This product is natural and has all the necessary ingredients for sustainable life which include Nitrogen, Phosphorus and potassium. Our main competitor would be plenty sprout. We would like like to see the colors blue, green and anything organic would suffice. The final design should draw in the customer with a uniqueness that will allow our customer to choose our product versus an industrial made product This label will be posted onto the bottle. We may need a webpage as well. I have attached the logo, Feel free to make changes, along with the required product details that will be displayed on the back of the bottle. I have attached an example of a product from another company Please add the webpage, Velmorafarms.com to the product label. Feel free to contact me at Velmorafarms@quillpost.com. The product name and tagline is as follows. Velmora Farm's Tidewell, Organic fertilizer.

Target Market(s)

Household Gardeners, Horticulturist, Farmers/Agriculture industry, Lawn care and Aquaponics

Industry/Entity Type

Industrial

Other font styles liked:
• Same Font as the logo file I sent

Requirements
Must have
• Webpage(VelmoraFarms.com)Chatterly Page emblem on label. The file attachment I added must be on the backside of the label. Organic Fertilizer Velmora Farm's Tidewell Logo(Feel Free to adjust or manipulate current logo.
Nice to have
• Recycled emblem

```html
<!DOCTYPE html>
<html lang="en">
<head>
<meta charset="utf-8">
<title>Velmora Farm's Tidewell Organic Fertilizer Label</title>
<link rel="stylesheet" href="https://fonts.googleapis.com/css2?family=Libre+Caslon+Text:wght@700&family=Arimo:ital,wght@0,700;1,700&display=swap">
<style>
  :root {
    --lime: #4dff0f;
    --leaf: #5ec41f;
    --forest: #2f8a12;
    --ink: #111111;
    --paper: #ffffff;
    --meadow-dark: #3f7a22;
    --meadow-light: #8fcf4a;
    --bloom: #8b5fd0;
  }
  html, body {
    margin: 0;
    padding: 0;
    width: 1200px;
    height: 1200px;
    overflow: hidden;
    background: var(--paper);
  }
  .label {
    position: relative;
    width: 1200px;
    height: 1200px;
    overflow: hidden;
  }
  .meadow-photo {
    position: absolute;
    inset: 0;
    background:
      radial-gradient(ellipse at 75% 4%, rgba(240, 210, 60, 0.55), transparent 22%),
      radial-gradient(ellipse at 50% 98%, rgba(150, 110, 220, 0.85), transparent 45%),
      radial-gradient(ellipse at 10% 40%, rgba(160, 120, 220, 0.7), transparent 20%),
      radial-gradient(ellipse at 92% 40%, rgba(170, 130, 230, 0.6), transparent 18%),
      linear-gradient(180deg, var(--meadow-light) 0%, var(--meadow-dark) 30%, #5a9a30 60%, var(--bloom) 100%);
  }
  .fence-panel {
    position: absolute;
    left: 0;
    top: 0;
    width: 1200px;
    height: 395px;
  }
  .brand-name {
    position: absolute;
    left: 0;
    width: 1200px;
    top: 170px;
    margin: 0;
    text-align: center;
    font-family: "Libre Caslon Text", Georgia, serif;
    font-weight: 700;
    font-size: 112px;
    line-height: 1;
    color: var(--leaf);
    letter-spacing: -1px;
  }
  .title-band {
    position: absolute;
    left: 28px;
    top: 442px;
    width: 1144px;
    height: 238px;
    background: var(--lime);
    display: flex;
    flex-direction: column;
    align-items: center;
    justify-content: center;
  }
  .product-title {
    margin: 0;
    font-family: "Libre Caslon Text", Georgia, serif;
    font-weight: 700;
    font-size: 78px;
    line-height: 1.22;
    color: var(--paper);
    text-align: center;
  }
  .detail-panel {
    position: absolute;
    left: 28px;
    top: 680px;
    width: 1144px;
    height: 388px;
    background: var(--paper);
    border-bottom: 8px solid var(--lime);
    box-sizing: content-box;
  }
  .benefits {
    list-style: none;
    margin: 0;
    padding: 0;
    font-family: "Arimo", Arial, sans-serif;
    font-style: italic;
    font-weight: 700;
    font-size: 29px;
    line-height: 41px;
    color: var(--ink);
  }
  .benefit {
    position: absolute;
    white-space: nowrap;
  }
  .benefit::before {
    content: "";
    position: absolute;
    left: -40px;
    top: 8px;
    width: 24px;
    height: 24px;
    border-radius: 50%;
    background: var(--leaf);
  }
  .benefit-one { left: 326px; top: 40px; }
  .benefit-two { left: 148px; top: 104px; }
  .benefit-three { left: 118px; top: 173px; text-align: center; }
  .website {
    position: absolute;
    left: 0;
    width: 1144px;
    top: 325px;
    margin: 0;
    text-align: center;
    font-family: "Arimo", Arial, sans-serif;
    font-weight: 700;
    font-size: 37px;
    color: var(--forest);
  }
  .recycle-mark {
    position: absolute;
    left: 16px;
    top: 318px;
    width: 50px;
    height: 50px;
    border-radius: 50%;
    background: var(--leaf);
  }
</style>
</head>
<body>
  <main class="label">
    <div class="meadow-photo" role="img" aria-label="Blurred garden of purple and white crocus flowers in green grass"></div>

    <svg class="fence-panel" viewBox="0 0 1200 395" aria-hidden="true">
      <path d="M0,135 L130,135 Q600,-50 1070,135 L1200,135 L1200,383 L0,383 Z" fill="#ffffff"/>
      <path d="M0,138 L130,138 Q600,-47 1070,138 L1200,138" fill="none" stroke="#5ec41f" stroke-width="6"/>
      <rect x="0" y="379" width="1200" height="5" fill="#5ec41f"/>
      <rect x="0" y="388" width="1200" height="4" fill="#4dff0f"/>
    </svg>

    <h2 class="brand-name">Velmora Farms</h2>

    <section class="title-band">
      <h1 class="product-title">Tidewell<br>Organic Fertilizer</h1>
    </section>

    <section class="detail-panel">
      <ul class="benefits">
        <li class="benefit benefit-one">Made from a vermiculture process</li>
        <li class="benefit benefit-two">Safe for vegetables, fruits, herbs, gardens and lawns</li>
        <li class="benefit benefit-three">This natural product is an alternative to oil based fertilizers<br>&nbsp;&nbsp;&nbsp;&nbsp;and has all the necessary ingredients for sustainable<br>&nbsp;&nbsp;life which include Nitrogen, Phosphorus and potassium.</li>
      </ul>
      <div class="recycle-mark" role="img" aria-label="Recycled emblem"></div>
      <p class="website">Velmorafarms.com</p>
    </section>
  </main>
</body>
</html>
```